依頼詳細
<現状サイトの課題>
①一目で、何をしている会社なのかが分からない。
⇒商品画像・作業画像などを入れ、分かりやすく目を引き付けるようにする。

②項目が小さく、引き付けにくいデザイン。
⇒アイコンを大きくして、デザイン性を持たせる。

③自社の強みを視覚化できていない。
⇒図や写真を追加し、視覚的に伝わるようにする。

④自社の新着情報がないので社内の動きが把握できない。
⇒新着ニュースを追加し社内の動きが把握できるようにする。

⑤企業規模が小さく感じてしまう。
⇒洗練されたデザイン、コンテンツの充実、グローバルサイトの作成により企業規模をワンランク大きく見えるように表現する。
----------------------------------
<現在のサイト>
明確なサイトの情報共有はできませんが、TOPページの情報を一部伏せて共有します。添付の”TOPページ”をご参照ください。

<サイトリニューアルの方針>
①強みを明確にする為、全体的に画像化し打ち出したい。TOPページは動画を掲載し、よりリアルにユーザー様にイメージが伝わるデザインにする。

②企業規模をワンランク大きく見えるように表現し、グローバル化についてもアピールすることで、事業規模の大きい信頼出来る会社であることが分かるようにし、新規顧客の獲得および定着するようにサイトリニューアルを行う。

③必須機能
・TOPページへ動画を埋め込む。
・スマホ対応(レスポンシブウェブデザイン)にする。
・ウェブ見積り機能を設け、いつでも見積りが確認できるようにする。(TOPページにバナーを設けるなどデザインする)

<イメージ参考サイト>
①メインカラーをブルーとし、TOPページを開くとすぐに大きな画像イメージが見えます。
https://www.e-harutsubo.co.jp/

②トップページに表示される、動画イメージです。
https://www.pelvo.co.jp/

③コンテンツの配置や施工事例が見やすいです。
http://www.satebi-kk.com/

④TOPページに施工写真や文字が挿入されており分かりやすい。また企業イメージがよく考えられており、ブランディングされています。
http://www.tsuganame.co.jp/

<カラーテーマ>
①青系(堅実・信頼・クール)または水色系(さわやか・清潔感)

②青4割、白6割の配色のイメージでお願いします。制作の際は、カラーチャート(カラーを選んだ理由)もご提示いただけると幸いです。

<重視する点/検討基準>
①サイトコンセプトにあったデザイン(ご提案の際は、制作頂いたデザインコンセプト及びデザイン説明コメントの記載をお願い致します)

②納期厳守

<具体的な制作数>
TOPページ:1ページ(PC版のデザイン制作をお願いします)

<選考の進め方>
ご提案頂いたデザイン内容・コンセプトなどをもとに、プロジェクトメンバーで選考、決定致します。
※今回は、トップページデザインのみの見積りとなります。
今後、コーディングを依頼する可能性もございます。その場合は改めてハルニーズを通じてご依頼させて頂きます。パララックスデザインでのコーディングも条件として入れてまいります。
ページ数
1ページ
希望イメージ
シンプル 複雑
単色 カラフル
暗い 明るい
日常 高級
遊び心 厳粛
未来的 伝統的
女性的 男性的
希望する色
青系、水色系
納品ファイル
• イラストレーター形式 (.ai)
• フォトショップ形式 (.psd)
追記です。
サイトコンセプトの資料も添付いたします。
宜しくお願いいたします。
■ 選んだ理由

クライアント様と協議させていただき、コンセプトに合った総合的なデザインを評価させて頂きました。
その中で、クライアント様からの評価が多かった「Pixfarn様」を当選とさせていただきました。ありがとうございました。

■ 提案者全員のお礼・コメント

ハルニーの皆さん、このように沢山の素敵なデザインをご提案頂き本当にありがとうございました。
コンセプトを基に、クライアント様とも大いに悩んで決定させて頂きました。
また、選定が期限間近になってしまいましたこと、申し訳ございませんでした。

機会があれば、今後ともどうぞ宜しくお願い致します。

```html
<!DOCTYPE html>
<html lang="ja">
<head>
<meta charset="utf-8">
<title>トップページ</title>
<link href="https://fonts.googleapis.com/css2?family=Noto+Sans+JP:wght@400;700;900&family=Roboto:wght@700;900&display=swap" rel="stylesheet">
<style>
:root{
  --blue:#1740d8;
  --blue-deep:#0b2a9e;
  --blue-light:#3f8fe0;
  --red:#e8212d;
  --black:#000;
  --ink:#222;
  --grey:#666;
  --line:#d6d6d6;
  --white:#fff;
}
*{box-sizing:border-box;margin:0;padding:0}
html,body{width:773px;height:1200px;overflow:hidden;background:var(--white)}
body{font-family:"Noto Sans JP",sans-serif;color:var(--ink);position:relative}
.wrap{width:515px;margin:0 auto;position:relative}

/* header */
.site-header{height:82px}
.site-header .wrap{display:flex;height:82px}
.brand{width:167px;background:var(--black);color:var(--white);display:flex;align-items:center;justify-content:center;font-size:30px;font-weight:700;letter-spacing:1px}
.header-copy{padding:8px 0 0 14px;flex:1}
.header-copy h1{font-size:11px;font-weight:700;color:var(--blue);margin-bottom:6px}
.header-copy p{font-size:6.5px;line-height:1.55;color:var(--grey)}

/* nav */
.global-nav{background:var(--blue);height:52px}
.global-nav ul{list-style:none;display:flex;height:52px}
.global-nav li{flex:1;display:flex;flex-direction:column;align-items:center;justify-content:center;color:var(--white);font-size:7px;gap:4px;border-right:1px solid rgba(255,255,255,.25)}
.global-nav li:first-child{border-left:1px solid rgba(255,255,255,.25)}
.global-nav svg{width:18px;height:16px}

/* hero */
.hero{background:var(--black);height:214px;overflow:hidden;position:relative}
.hero .movie{position:absolute;font-family:Roboto,sans-serif;font-weight:900;font-size:52px;color:#3a3a3a;transform:rotate(-8deg);letter-spacing:2px}
.hero .wrap{padding-top:16px;z-index:1}
.hero h2{font-family:Roboto,sans-serif;font-weight:900;color:var(--white);font-size:25px;line-height:1.45}
.hero p{color:var(--white);font-weight:700;font-size:13px;line-height:1.4;margin-top:10px;width:200px;word-break:break-all}

/* strengths */
.strengths{height:200px;position:relative}
.strengths .tiles{position:absolute;inset:0;background:linear-gradient(135deg,#7ab8f5 0%,#2b6fe0 45%,#0c3fc0 100%)}
.label{display:block;width:113px;margin:0 auto;text-align:center;color:var(--white);font-size:7px;padding:5px 0}
.label.red{background:var(--red)}
.label.blue{background:var(--blue)}
.strengths .label{position:relative;top:10px}
.points{position:relative;display:flex;justify-content:space-around;width:515px;margin:26px auto 0}
.point{width:118px;height:118px;border-radius:50%;background:var(--white);display:flex;flex-direction:column;align-items:center;justify-content:center;text-align:center;border:3px solid rgba(255,255,255,.6)}
.point b{font-family:Roboto,sans-serif;font-size:32px;color:var(--blue);line-height:1}
.point span{font-size:9.5px;font-weight:700;color:var(--blue-deep);line-height:1.35;margin-top:4px}

/* news */
.news{padding-top:18px}
.cards{display:flex;justify-content:space-between;margin-top:16px}
.card{width:162px;height:208px;padding:0;position:relative}
.card.active{outline:2px solid var(--blue);outline-offset:2px}
.card .photo{height:84px;background:var(--black);display:flex;align-items:center;justify-content:center;color:var(--white);font-family:Roboto,sans-serif;font-weight:900;font-size:17px;position:relative}
.date{position:absolute;left:0;bottom:-6px;background:var(--red);color:var(--white);font-size:6.5px;padding:2px 8px}
.card h3{font-size:8.5px;font-weight:700;line-height:1.45;margin:14px 6px 6px}
.card p{font-size:6.5px;color:var(--grey);line-height:1.6;margin:0 6px}
.more{display:inline-block;border:1px solid var(--line);font-size:6.5px;padding:3px 12px;margin:8px 6px 0;color:var(--ink)}

.archive{margin-top:10px;height:34px;border:1px solid var(--line);display:flex;align-items:center;justify-content:center;position:relative}
.archive span{border:1px solid var(--blue);color:var(--blue);font-size:7px;padding:5px 18px;background:var(--white)}
.archive svg{position:absolute;right:0;top:-1px;height:34px;width:40px}

/* works */
.works{margin-top:16px;display:flex;height:140px}
.works .photo{width:245px;background:var(--black);color:var(--white);display:flex;align-items:center;justify-content:center;font-family:Roboto,sans-serif;font-weight:900;font-size:24px}
.works .body{flex:1;padding:0 0 0 12px}
.works .label{margin:0;width:56px}
.works h3{font-size:10px;font-weight:700;line-height:1.5;margin:10px 0 6px}
.works p{font-size:6.5px;color:var(--grey);line-height:1.6}
.works .more{margin:10px 0 0}

/* footer */
.site-footer{position:absolute;left:0;right:0;bottom:0;height:176px}
.site-footer .tiles{position:absolute;inset:0;background:linear-gradient(160deg,#5fa4ee 0%,#1f5fd6 50%,#0a2f9c 100%)}
.site-footer .wrap{display:flex;padding-top:14px;color:var(--white)}
.footer-info{width:250px}
.footer-info .brand-name{font-size:48px;font-weight:700;letter-spacing:2px;line-height:1;padding-left:70px}
.footer-info p{font-size:6.5px;line-height:1.7;margin-top:10px;padding-left:0}
.footer-links{flex:1;display:flex;gap:26px;padding:6px 0 0 50px}
.footer-links ul{list-style:none;font-size:6.5px;line-height:1.8}
.copyright{position:absolute;left:0;right:0;bottom:0;height:14px;background:var(--blue-deep);color:var(--white);font-size:6px;text-align:center;line-height:14px}
</style>
</head>
<body>

<header class="site-header">
  <div class="wrap">
    <div class="brand">LOGO</div>
    <div class="header-copy">
      <h1>クオリティーの高い施工製品を短納期でご提供いたします。</h1>
      <p>私たちは確かな技術と柔軟な対応力で、お客様のご要望に<br>丁寧にお応えいたします。設計から施工、アフターサービスまで<br>一貫した体制で、安心と信頼をお届けいたします。</p>
    </div>
  </div>
</header>

<nav class="global-nav">
  <ul class="wrap">
    <li><svg viewBox="0 0 18 16" fill="none" stroke="#fff" stroke-width="1.4"><path d="M2 15V6l7-4 7 4v9z"/><path d="M7 15v-5h4v5"/></svg>会社概要</li>
    <li><svg viewBox="0 0 18 16" fill="none" stroke="#fff" stroke-width="1.4"><rect x="2" y="4" width="14" height="10"/><path d="M6 4V2h6v2"/></svg>事業紹介</li>
    <li><svg viewBox="0 0 18 16" fill="none" stroke="#fff" stroke-width="1.4"><rect x="3" y="1" width="12" height="14"/><path d="M6 5h6M6 8h6M6 11h4"/></svg>WEB見積り</li>
    <li><svg viewBox="0 0 18 16" fill="none" stroke="#fff" stroke-width="1.4"><path d="M1 15h16M3 15V8l4-3v10M7 15V3l8 4v8"/></svg>施工実績</li>
    <li><svg viewBox="0 0 18 16" fill="none" stroke="#fff" stroke-width="1.4"><circle cx="9" cy="5" r="3"/><path d="M3 15c0-4 3-6 6-6s6 2 6 6"/></svg>スタッフ紹介</li>
    <li><svg viewBox="0 0 18 16" fill="none" stroke="#fff" stroke-width="1.4"><circle cx="6" cy="5" r="2.5"/><circle cx="12" cy="5" r="2.5"/><path d="M1 14c0-3 2-5 5-5s5 2 5 5M9 10c1-1 2-1 3-1 3 0 5 2 5 5"/></svg>採用情報</li>
    <li><svg viewBox="0 0 18 16" fill="none" stroke="#fff" stroke-width="1.4"><path d="M3 13l1-4 8-8 3 3-8 8z"/><path d="M2 15h14"/></svg>ブログ</li>
    <li><svg viewBox="0 0 18 16" fill="none" stroke="#fff" stroke-width="1.4"><rect x="1" y="3" width="16" height="11"/><path d="M1 3l8 6 8-6"/></svg>お問い合わせ</li>
  </ul>
</nav>

<section class="hero" role="img" aria-label="会社紹介動画の表示エリア">
  <span class="movie" style="left:-10px;top:80px">MOVIE</span>
  <span class="movie" style="left:290px;top:120px">MOVIE</span>
  <span class="movie" style="left:570px;top:60px">MOVIE</span>
  <div class="wrap">
    <h2>Speedy<br>High Quality<br>Flexible</h2>
    <p>sampletextsampletextsampletextsampletextsampletextsampletextsampletextsampletextsampleten...</p>
  </div>
</section>

<section class="strengths">
  <div class="tiles" role="img" aria-label="青いタイル状の背景写真"></div>
  <span class="label red">当社の3つの強み</span>
  <div class="points">
    <div class="point"><b>1</b><span>高品質・短納期<br>でご提供いたします<br>サービス</span></div>
    <div class="point"><b>2</b><span>何でもご相談<br>いただける<br>柔軟な体制</span></div>
    <div class="point"><b>3</b><span>常にお客様目線で<br>取り組み<br>成長し続ける企業</span></div>
  </div>
</section>

<main class="wrap news">
  <span class="label blue">新着情報</span>
  <div class="cards">
    <article class="card active">
      <div class="photo" role="img" aria-label="お知らせの写真">PHOTO<span class="date">2015.07.25</span></div>
      <h3>サンプルタイトルですサンプルタイトルですサンプルタイトルです…</h3>
      <p>サンプルテキストですサンプルテキストですサンプルテキストですサンプルテキストです…</p>
      <a class="more">詳しく見る</a>
    </article>
    <article class="card">
      <div class="photo" role="img" aria-label="お知らせの写真">PHOTO<span class="date">2015.07.25</span></div>
      <h3>サンプルタイトルですサンプルタイトルですサンプルタイトルです…</h3>
      <p>サンプルテキストですサンプルテキストですサンプルテキストですサンプルテキストです…</p>
      <a class="more">詳しく見る</a>
    </article>
    <article class="card">
      <div class="photo" role="img" aria-label="お知らせの写真">PHOTO<span class="date">2015.07.25</span></div>
      <h3>サンプルタイトルですサンプルタイトルですサンプルタイトルです…</h3>
      <p>サンプルテキストですサンプルテキストですサンプルテキストですサンプルテキストです…</p>
      <a class="more">詳しく見る</a>
    </article>
  </div>

  <div class="archive">
    <span>過去の実績一覧</span>
    <svg viewBox="0 0 40 34" fill="none" stroke="#d6d6d6" stroke-width="1"><path d="M0 0l16 17L0 34"/></svg>
  </div>

  <section class="works">
    <div class="photo" role="img" aria-label="施工事例の写真">PHOTO</div>
    <div class="body">
      <span class="label red">施工事例</span>
      <h3>サンプルタイトルですサンプルタイトルですサンプルタイトルです…</h3>
      <p>サンプルテキストですサンプルテキストですサンプルテキストですサンプルテキストですサンプルテキストです…</p>
      <a class="more">詳しく見る</a>
    </div>
  </section>
</main>

<footer class="site-footer">
  <div class="tiles" role="img" aria-label="青いタイル状の背景写真"></div>
  <div class="wrap">
    <div class="footer-info">
      <div class="brand-name">LOGO</div>
      <p>本社<br>〒000-0000 サンプル県サンプル市サンプル町0-0-0<br>TEL 000-000-0000 / FAX 000-000-0000<br>営業時間 9:00〜18:00（土日祝休）</p>
    </div>
    <div class="footer-links">
      <ul><li>会社概要</li><li>事業紹介</li><li>WEB見積り</li><li>施工実績</li><li>スタッフ紹介</li></ul>
      <ul><li>採用情報</li><li>ブログ</li><li>新着情報</li><li>施工事例</li><li>お問い合わせ</li></ul>
      <ul><li>プライバシー</li><li>サイトマップ</li></ul>
    </div>
  </div>
  <div class="copyright">Copyright © 0000 Sample Co., Ltd. All Rights Reserved.</div>
</footer>

</body>
</html>
```